Shopping center investment profile

We need to design a two-page 8.5" x 11" brochure that can be used as a template for profiling our shopping centers and demonstrating our track record to investors.

Our company (Pelvoran Real Estate Investments) owns retail shopping centers in the southwestern United States. Our website is www.kelvistrand.example, but we will be redesigning and modernizing the website and logo in the near future, so please do not use the color schemes or framework of the website for the brochure.

Our investors are institutional and high net worth investors who typically have an existing relationship with our company. They are determining whether to invest multi-millions of dollars in a shopping center opportunity, so the brochure needs to be professional, very high quality and provide key information about the specific property.
Updates

Additional guidance on color scheme:

We would like to see a Blue (something like Hex #5A61BC) and Gold (Hex #EDB215) or (Hex #DDA24B) color scheme with some Black accents 

Thank you!

Target Market(s)

Our target audiences are institutional investors, high net-worth individuals, financial firms and medium to large commercial real estate companies.

Industry/Entity Type

Investment

Requirements
Must have
• Clean and modern look with corresponding fonts and colors.
• Incorporates the information found in the attached "Morrowick Commons profile" Pages or PDF file.
• Final file design files that can be modified easily
Nice to have
• Two examples of industry brochures are attached. These are examples of the professional quality that we are looking for, not necessarily the design or format.

```html
<!DOCTYPE html>
<html lang="en">
<head>
<meta charset="utf-8">
<title>Morrowick Commons – Property Profile</title>
<link rel="stylesheet" href="https://fonts.googleapis.com/css2?family=Oswald:wght@500&family=Questrial&family=Mulish:wght@700&display=swap">
<style>
  :root{
    --blue:#5a61bc;
    --gold:#edb215;
    --gold-light:#f9dd9c;
    --gold-row:#ecb426;
    --grey-bg:#efeff1;
    --grey-row:#f1f1f1;
    --grey-row-dark:#cacacc;
    --ink:#222;
    --black:#050505;
    --white:#fff;
  }
  *{box-sizing:border-box;margin:0;padding:0}
  html,body{width:927px;height:1200px;overflow:hidden}
  body{background:var(--grey-bg);font-family:"Questrial",sans-serif;color:var(--ink)}
  .page{position:relative;width:927px;height:1200px;overflow:hidden}
  .backdrop{position:absolute;inset:0}
  .property-title{position:absolute;left:14px;top:6px;font-family:"Oswald",sans-serif;font-weight:500;
    font-size:56px;line-height:60px;color:var(--blue);text-transform:uppercase;letter-spacing:.5px}
  .property-kicker{position:absolute;left:14px;top:166px;font-size:20px;letter-spacing:4.5px;color:var(--blue)}
  .section-banner{position:absolute;height:66px;background:var(--gold);color:var(--white);
    font-family:"Oswald",sans-serif;font-weight:500;font-size:34px;line-height:66px;padding-left:32px;
    clip-path:polygon(28px 0,100% 0,calc(100% - 28px) 100%,0 100%)}
  .banner-results{left:77px;top:213px;width:248px}
  .banner-opportunity{left:335px;top:458px;width:264px}
  .results-list{position:absolute;left:12px;top:304px;width:470px;list-style:none;font-size:15.2px;line-height:18.5px}
  .results-list li{padding-left:18px;text-indent:-18px}
  .results-list li::before{content:"•";display:inline-block;width:18px;text-indent:0}
  .opportunity-list{position:absolute;left:14px;top:530px;width:880px;list-style:none;font-size:15.2px;line-height:20.6px}
  .opportunity-list li::before{content:"•";display:inline-block;width:32px}
  .data-table{position:absolute;border-collapse:collapse;font-size:17px}
  .data-table caption{background:var(--black);color:var(--white);font-family:"Mulish",sans-serif;font-weight:700;
    font-size:24px;height:46px;line-height:46px;text-align:center}
  .data-table td{padding:0 10px}
  .data-table td:last-child{text-align:right}
  .summary{left:14px;top:791px;width:447px}
  .summary tr{height:39px}
  .summary tr:nth-child(odd){background:var(--gold-light)}
  .summary tr:nth-child(even){background:var(--gold-row)}
  .summary tr.irr{height:68px;line-height:22px}
  .investment{left:474px;top:790px;width:442px;font-size:15px}
  .investment tr{height:33px}
  .investment tr:nth-child(odd){background:var(--grey-row)}
  .investment tr:nth-child(even){background:var(--grey-row-dark)}
  .investment tr.total td{text-align:center;font-size:17px}
  .investment tr.structure{height:77px;line-height:21px}
</style>
</head>
<body>
<div class="page">
  <svg class="backdrop" width="927" height="1200" viewBox="0 0 927 1200">
    <defs>
      <linearGradient id="sky-lot" x1="0" y1="0" x2="0" y2="1">
        <stop offset="0" stop-color="#c9d8ea"/>
        <stop offset=".45" stop-color="#c7b39c"/>
        <stop offset="1" stop-color="#8d8880"/>
      </linearGradient>
      <linearGradient id="render" x1="0" y1="0" x2="0" y2="1">
        <stop offset="0" stop-color="#eef2f6"/>
        <stop offset=".5" stop-color="#9a5a48"/>
        <stop offset="1" stop-color="#5e7a3e"/>
      </linearGradient>
    </defs>
    <polygon points="0,700 927,640 927,695 0,748" fill="#ffffff"/>
    <polygon points="0,748 927,695 927,1200 0,1200" fill="#5a61bc"/>
    <polygon points="300,0 655,0 510,284 300,284 248,160" fill="url(#sky-lot)" role="img" aria-label="Photo of the shopping center storefronts and parking lot"/>
    <polygon points="602,108 927,108 927,620 640,620 517,380 565,250" fill="url(#render)" role="img" aria-label="Rendering of the renovated storefront facade with trees"/>
  </svg>

  <h1 class="property-title">Morrowick<br>Commons</h1>
  <p class="property-kicker">PROPERTY PROFILE</p>

  <h2 class="section-banner banner-results">RESULTS</h2>
  <ul class="results-list">
    <li>Stabilized the shopping center within three years, producing excellent results for investors</li>
    <li>Transformed the center into a vibrant destination that the surrounding community is excited about</li>
    <li>Transitioned legacy tenants to upgrade the business operators</li>
    <li>Reduced the shopping center’s operating expenses by replacing vendors and appealing property taxes</li>
  </ul>

  <h2 class="section-banner banner-opportunity">OPPORTUNITY</h2>
  <ul class="opportunity-list">
    <li>Bank owned property with attractive purchase price</li>
    <li>Strong relationship with seller’s broker and decision makers</li>
    <li>Redevelopment upside with management and leasing</li>
    <li>No major renovations required</li>
    <li>Ashburne location has very strong population, education and income demographics</li>
    <li>Adjacent to premier 2,500-residence master planned community of Larkmere Shores</li>
    <li>Strong employment area with the new Corvane Gateway hospital and the adjacent Hallidane Cancer center</li>
  </ul>

  <table class="data-table summary">
    <caption>Summary</caption>
    <tr><td>Property Type</td><td>Shopping Center</td></tr>
    <tr><td>Size</td><td>79,490 sq ft</td></tr>
    <tr><td>Purchased</td><td>April 2011</td></tr>
    <tr><td>Total Investment</td><td>$X,XXX,XXX</td></tr>
    <tr><td>Purchase Occupancy</td><td>8.39%</td></tr>
    <tr><td>Current Occupancy</td><td>97.29%</td></tr>
    <tr class="irr"><td>Projected 5-year IRR<br>(Unleveraged)</td><td>XX.XX%</td></tr>
  </table>

  <table class="data-table investment">
    <caption>Investment Information</caption>
    <tr><td>Purchase Price</td><td>$X,XXX,XXX</td></tr>
    <tr><td>Sponsor Acquisition Fee</td><td>$XX,XXX</td></tr>
    <tr><td>Painting and Landscape</td><td>$XXX,XXX</td></tr>
    <tr><td>TI/LC Reserve</td><td>$X,XXX,XXX</td></tr>
    <tr><td>Operating Expenses</td><td>$XXX,XXX</td></tr>
    <tr class="total"><td colspan="2">Total Cash Investment</td></tr>
    <tr><td>Investor / Sponsor Split</td><td>XX% / XX%</td></tr>
    <tr class="structure"><td>Structure</td><td>• Cash Flow Pari Passu<br>• Acquisition Fee<br>• Management Fee</td></tr>
  </table>
</div>
</body>
</html>
```